Visitenkarten-Design für Sonnen-/Fensterschutz
Zielgruppe
KLT GmbH ist eine Firma, die Sonnenschutz und Fensterschutz anbieten.
'Ihr kompetenter Partner in Sachen Sonnenschutz- , Fenster- und Türtechnik. Sie erhalten echtes Handwerk aus dem Mühlviertel zu fairen Preisen.'
Unsere Zielgruppe sind Personen mit Haus, die am Land leben.
Firmenname: KLT GmbH
Slogan: Fenster & Sonnenschutz
Aufgabenstellung
Hier befindet sich das Logodesign: https://bx.qz/r-WuPoN7TkRm
Bitte ein schlichtes Design bereitstellen mit einer Dummy-Person:
Max Mustermann + Telefonnummer + Email
Die finalen Daten bitte erst am Schluss berücksichtigen (für Gewinnerdesign)
Gerne auch hintern + vorne bedruckbar bereitstellen.

```html
<!DOCTYPE html>
<html lang="de">
<head>
<meta charset="utf-8">
<title>KLT GmbH – Visitenkarte</title>
<link rel="stylesheet" href="https://fonts.googleapis.com/css2?family=Poppins:wght@400;700&family=Source+Sans+3:wght@400;600&display=swap">
<style>
  :root {
    --stage: #595959;
    --paper: #ffffff;
    --orange: #ef7d1a;
    --red: #e33c22;
    --text: #5a5a5a;
    --rule: #f3c9a8;
  }
  * { box-sizing: border-box; margin: 0; padding: 0; }
  html, body { width: 1200px; height: 1200px; overflow: hidden; }
  body { background: var(--stage); position: relative; font-family: "Poppins", sans-serif; }

  .card { position: absolute; left: 247px; width: 668px; height: 432px; background: var(--paper); overflow: hidden; }
  .card--front { top: 112px; }
  .card--back { top: 618px; display: flex; align-items: center; justify-content: center; }

  .speed-lines { position: absolute; left: 0; top: 56px; }

  .brand { position: absolute; left: 372px; top: 46px; width: 264px; text-align: right; }
  .brand__name { font-family: "Poppins", sans-serif; font-weight: 700; font-size: 46px; line-height: 1; color: var(--red); letter-spacing: 2px; }
  .brand__slogan { font-family: "Poppins", sans-serif; font-weight: 700; font-size: 12px; color: var(--red); text-transform: uppercase; margin-top: 6px; letter-spacing: .3px; }

  .person { position: absolute; left: 30px; width: 274px; top: 220px; text-align: center; font-family: "Source Sans 3", sans-serif; color: var(--text); }
  .person__name { font-size: 25px; font-weight: 400; line-height: 1.2; }
  .person__role { font-size: 18px; font-weight: 600; margin-top: 6px; }

  .divider { position: absolute; left: 325px; top: 199px; width: 1px; height: 140px; background: var(--rule); }

  .contact { position: absolute; left: 386px; top: 200px; color: var(--text); font-size: 18px; line-height: 1.1; }
  .contact__company { font-size: 15px; font-weight: 700; color: #8a8a8a; letter-spacing: 1px; margin-bottom: 10px; }
  .contact__row { display: flex; align-items: flex-start; gap: 6px; margin-bottom: 12px; }
  .contact__row svg { flex: none; margin-top: 1px; }

  .bottom-band { position: absolute; left: 0; top: 400px; width: 668px; height: 13px; background: linear-gradient(90deg, var(--orange), var(--red)); }

  .back-brand { font-family: "Poppins", sans-serif; font-weight: 700; font-size: 110px; color: var(--red); letter-spacing: 4px; line-height: 1; }
</style>
</head>
<body>
  <section class="card card--front">
    <svg class="speed-lines" width="400" height="50" viewBox="0 0 400 50" aria-hidden="true">
      <defs>
        <linearGradient id="lineGrad" x1="0" x2="1">
          <stop offset="0" stop-color="#ef7d1a"/><stop offset="1" stop-color="#e33c22"/>
        </linearGradient>
      </defs>
      <rect x="0" y="4" width="360" height="4" fill="url(#lineGrad)"/>
      <rect x="0" y="17" width="375" height="6" fill="url(#lineGrad)"/>
      <rect x="0" y="32" width="390" height="9" fill="url(#lineGrad)"/>
    </svg>

    <div class="brand">
      <div class="brand__name">KLT</div>
      <div class="brand__slogan">Fenster &amp; Sonnenschutz</div>
    </div>

    <div class="person">
      <div class="person__name">Max Mustermann</div>
      <div class="person__role">Geschäftsführer</div>
    </div>

    <div class="divider"></div>

    <div class="contact">
      <div class="contact__company">KLT GmbH</div>
      <div class="contact__row">
        <svg width="22" height="22" viewBox="0 0 22 22" aria-hidden="true"><path d="M1 3 L21 11 L1 20 L6 11 Z" fill="var(--red)"/></svg>
        <div>Am Lindenhang 7<br>4020 Musterstadt</div>
      </div>
      <div class="contact__row">
        <svg width="22" height="22" viewBox="0 0 22 22" aria-hidden="true"><path d="M5 2 L9 2 L10 7 L7 9 C8 12 10 14 13 15 L15 12 L20 13 L20 17 C20 19 18 20 16 20 C8 19 3 14 2 6 C2 4 3 2 5 2 Z" fill="var(--red)"/></svg>
        <div>+49 170 555 0123</div>
      </div>
      <div class="contact__row">
        <svg width="22" height="22" viewBox="0 0 22 22" aria-hidden="true"><rect x="1" y="5" width="20" height="14" rx="1" fill="var(--red)"/><path d="M2 6 L11 13 L20 6" fill="none" stroke="#fff" stroke-width="1.6"/></svg>
        <div>+49 170 555 0123</div>
      </div>
    </div>

    <div class="bottom-band"></div>
  </section>

  <section class="card card--back">
    <div class="back-brand">KLT GmbH</div>
  </section>
</body>
</html>
```